BELMORA needs a label for a Surface Cleaner with Alcohol

INTRODUCTION:
We are BELMORA, an experienced Spanish family-owned business specialized in manufacturing and distributing low-cost high-quality cleaning products in Spain, France and Portugal.

We are launching a new SURFACE CLEANER WITH ALCOHOL and we need an eye-catching label! We want to put your creativity to work! :D

CONCEPT:
Surface cleaner containing alcohol (not a disinfectant or hand sanitizer)

2 sizes

1) 750 ml PET cilinder white bottle with spray (bottle measures: 70mm diameter 230 mm height w/o spray)
Labels size (120mm base x 160mm height), 1 front label + 1 back label

2) 60 ml PET cilinder white bottle with spray (bottle 90mm height w/o spray x 35mm diameter) 1 label
Label size 110mm base x 60mm height

The design of the larger bottle must be adapted to the smaller bottle so as to make a collection

Label is in Spanish language (we are providing texts below)

GOAL:
To create a clean minimalist label with a “pharmaceutical” look and feel. Ideally by using colors and shapes to evoke a pharma green cross without explicitly using it. The pharma look and feel has to be visible from some distance. It must inspire safety and protection.

If you do mockups please use a 3D image of a bottle with sprayer (not the photo attached because it will look bad)

We love to see your ideas and be surprised with your proposals!

Thank you!

Target Market(s)

General public (non-professional) target, drugstore/supermaket, Spanish market mainly at the moment

Industry/Entity Type

Cleaning Product

Requirements
Must have
• Label front must have:
• - words: "LIMPIADOR HIGIENIZANTE" and "con ALCOHOL"
• - colors: white, pharma-looking light green, and a touch of blue
• - logo: BELMORA (brand), with the same pharma-looking green color
• - for the small bottle: a plane icon to point out that is suitable for travelling
• Label back side must contain this:
• - marketing text:
• “Limpiador higienizante para todo tipo de superfícies lavables. Su gran poder limpiador e higienizante elimina eficazmente la suciedad de zonas de contacto tales como asientos, inodoros, duchas, vidrios, pomos, manetas, asideros, barandillas, mesas, encimeras, suelos, mostradores, vitrinas, etc. No contiene lejía.”
• - icons:
• A column of 4-5 minimalist icons to clearly point out the applications (door knobs, seats, sink, handrail, toilet, floor, shower, glass,…) see icon examples attached for styling inspiration
• - legal text:
• “Líquido y vapores muy inflamables. Provoca irritación ocular grave. Puede provocar somnolencia o vértigo. Mantener alejado del calor, de superficies calientes, de chispas, de llamas abiertas y de cualquier otra fuente de ignición. No fumar. Mantener el recipiente herméticamente cerrado. Evitar respirar el polvo/el humo/el gas/la niebla/los vapores/el aerosol. Llevar guantes/prendas/gafas/máscara de protección. En caso de incendio emplear niebla de agua, espuma, productos químicos secos o dióxido de carbono ( CO2 ) para apagarlo. Almacenar en un lugar bien ventilado. Mantener el recipiente cerrado herméticamente. Mantener en lugar fresco.”
• - company identification:
• VESTA CORIN PRO SL
• B73925816
• C/ Valdemar 317 2-4
• 08147 Barcelona
• - pictograms: see the pictograms file
Nice to have
• Would be great to include:
• - seal: round seal with one or two words inside to give the feeling of “certified” or “approved”
• - a percetage number, like "100 % efectivo”
• - a small red “plus” sign referring for example to “+ higiene”
Should not have
• A plain green or red cross alone

```html
<!DOCTYPE html>
<html lang="es">
<head>
<meta charset="utf-8">
<title>BELMORA – Limpiador Higienizante</title>
<link rel="stylesheet" href="https://fonts.googleapis.com/css2?family=Noto+Serif:wght@700&family=Roboto:wght@400;700&display=swap">
<style>
  :root {
    --green: #3cb44a;
    --green-soft: #a9dcae;
    --white: #ffffff;
    --blue-soft: #8fd3f2;
    --red: #e4262b;
    --ink: #3d8f45;
    --canvas: #ffffff;
  }
  * { box-sizing: border-box; margin: 0; padding: 0; }
  html, body { width: 1200px; height: 1200px; overflow: hidden; background: var(--canvas); }
  .label {
    position: absolute; left: 52px; top: 325px;
    width: 1096px; height: 550px;
    background: var(--white);
    font-family: "Roboto", Arial, sans-serif;
  }
  .label-shapes { position: absolute; inset: 0; }
  .brand-name {
    position: absolute; left: 123px; top: 184px;
    font-family: "Noto Serif", Georgia, serif; font-weight: 700;
    font-size: 76px; line-height: 1; color: var(--green);
    letter-spacing: -1px;
  }
  .product-name {
    position: absolute; left: 133px; top: 273px;
    font-weight: 700; font-size: 19.5px; color: var(--green); line-height: 1;
  }
  .product-note {
    position: absolute; left: 205px; top: 296px;
    font-size: 15.5px; color: var(--green); line-height: 1;
  }
  .back-copy {
    position: absolute; left: 588px; top: 110px; width: 502px;
    font-size: 11.3px; line-height: 15px; color: var(--ink);
    text-align: justify;
  }
  .legal-title {
    margin-top: 6px;
    font-weight: 700; font-size: 17px; line-height: 19px; color: var(--green);
  }
  .company {
    position: absolute; left: 588px; top: 328px;
    font-size: 11.3px; line-height: 14.5px; color: var(--ink);
    font-style: normal;
  }
</style>
</head>
<body>
<div class="label">
  <svg class="label-shapes" width="1096" height="550" viewBox="0 0 840 422" aria-hidden="true">
    <!-- top green band -->
    <polygon points="0,0 840,0 840,17 0,132" fill="var(--green)"/>
    <line x1="0" y1="116" x2="840" y2="3" stroke="var(--white)" stroke-width="1.5"/>
    <!-- bottom green band -->
    <polygon points="0,404 840,254 840,422 0,422" fill="var(--green)"/>
    <line x1="0" y1="396" x2="840" y2="246" stroke="var(--green)" stroke-width="1.5"/>

    <!-- brand mark -->
    <circle class="brand-dot" cx="216" cy="82" r="62" fill="var(--green-soft)"/>

    <!-- volume drop -->
    <path d="M212 250 C200 280 169 300 169 330 A43 43 0 0 0 255 330 C255 300 224 280 212 250 Z" fill="var(--green)"/>
    <text x="212" y="341" text-anchor="middle" font-family="Roboto, Arial, sans-serif" font-weight="700" font-size="20" fill="var(--white)">750 ml</text>

    <!-- blue plus accent -->
    <path d="M300 238 h24 v38 h30 v24 h-30 v40 h-24 v-40 h-30 v-24 h30 Z" fill="var(--blue-soft)" opacity="0.85"/>

    <!-- red plus + higiene -->
    <path d="M33 323 h14 v14 h13 v14 h-13 v14 h-14 v-14 h-13 v-14 h13 Z" fill="var(--red)"/>
    <text x="60" y="378" font-family="Roboto, Arial, sans-serif" font-weight="700" font-size="14" fill="var(--red)">higiene</text>

    <!-- social marks -->
    <rect x="562" y="254" width="22" height="22" rx="3" fill="var(--green)"/>
    <circle cx="621" cy="265" r="11" fill="var(--green)"/>
    <rect x="656" y="254" width="22" height="22" rx="3" fill="var(--green)"/>

    <!-- application icons -->
    <g class="use-icons" fill="none" stroke="var(--white)" stroke-width="2.4" stroke-linejoin="round" stroke-linecap="round">
      <!-- toilet -->
      <rect x="456" y="342" width="12" height="20" rx="1.5"/>
      <path d="M468 360 h24 q0 12 -14 15 v10 h-10 v-25"/>
      <!-- stairs -->
      <polyline points="534,387 534,377 544,377 544,367 554,367 554,357 564,357 564,347 574,347 574,387 534,387"/>
      <line x1="536" y1="364" x2="574" y2="334"/>
      <!-- sink -->
      <path d="M594 360 h40 q-2 14 -20 16 q-18 -2 -20 -16 Z"/>
      <path d="M610 376 v11 h8 v-11"/>
      <path d="M614 360 v-10 q0 -5 7 -5 v4"/>
      <!-- door handle -->
      <rect x="676" y="343" width="13" height="43" rx="3"/>
      <rect x="656" y="352" width="30" height="7" rx="3.5"/>
      <circle cx="682.5" cy="374" r="2"/>
      <!-- seat -->
      <path d="M734 343 q-3 0 -2 4 l7 26 h24"/>
      <path d="M741 368 h16 q4 0 4 4"/>
      <path d="M748 373 v13 M742 386 h14"/>
    </g>
  </svg>

  <div class="brand-name">belmora</div>
  <div class="product-name">LIMPIADOR HIGIENIZANTE</div>
  <div class="product-note">containing alcohol</div>

  <div class="back-copy">
    <p class="marketing-text">Limpiador higienizante para todo tipo de superfícies lavables. Su gran poder limpiador e higienizante elimina eficazmente la suciedad de zonas de contacto tales como asientos, inodoros, duchas, vidrios, pomos, manetas, asideros, barandillas, mesas, encimeras, suelos, mostradores, vitrinas, etc. No contiene lejía.</p>
    <h2 class="legal-title">Legal Issue:</h2>
    <p class="legal-text">Líquido y vapores muy inflamables. Provoca irritación ocular grave. Puede provocar somnolencia o vértigo. Mantener alejado del calor, de superficies calientes, de chispas, de llamas abiertas y de cualquier otra fuente de ignición. No fumar. Mantener el recipiente herméticamente cerrado. Evitar respirar el polvo/el humo/el gas/la niebla/los vapores/el aerosol. Llevar guantes/prendas/gafas/máscara de protección. En caso de incendio emplear niebla de agua, espuma, productos químicos secos o dióxido de carbono ( CO2 ) para apagarlo. Almacenar en un lugar bien ventilado. Mantener el recipiente cerrado herméticamente. Mantener en lugar fresco.</p>
  </div>

  <address class="company">
    VESTA CORIN PRO SL<br>
    B73925816<br>
    C/ Valdemar 317 2-4<br>
    08147 Barcelona
  </address>
</div>
</body>
</html>
```